Korvix App Graphics Design

Our application promotes location based self expression via pictures and text. The primary focus of the application is on the content posted and not on the person that posted it.

We want a very clean and fresh design that evokes positive energy. Our site is unique so our design should be as well. People will reveal thoughts on our site, so the design should convey a "revealing" feel. Our site is a place where people are comfortable to freely express themselves. Colors we have in mind are blue and green hues with earth tones for background.

Our project is to design ten screens for our Korvix application at resolution of 1136-by-640 pixels:

Feed Screen
Camera Screen
Post Screen
Check In Screen
Approval Screen
Map Screen
Flag Screen
Feed Select Screen
Export Screen
Menu Screen

In the contest phase we will require only three screens to be submitted. The screens we require to be submitted are: Feed Screen; Map Screen and Camera Screen. The designer we select as the winner of the competition will then complete the project and deliver a total of the ten screens described above in the handover phase.

We have attached a document below with detailed specs of each screen, we ask for your innovation to bring these screens to life through your design.
Updates

We want to clarify one aspect regarding the VISOR: the visor needs to be transparent so that when the picture scrolls underneath it, you can still see the picture underneath the visor.

Hi Everyone,

We have noticed that some designers need clarification regarding the visor element in the feed screen.
I have attached two examples to our brief area called:
Visor Example 1 and Visor Example 2

Please note that these are not the style we are looking for but are a good example to the concept of a Transparent Visor above the feed stream. We are looking for you guys to come up with a Visor concept that is consistent with the style of the design you are submitting.

Thanks,

Bo

Target Market(s)

People 17-40 who want to share their thought about the world around them.

Industry/Entity Type

Flag

Font styles to use
Sans Serif
Other font styles liked:
• We like “Helvetica New” or “Avenir” but are flexible

Requirements
Must have
• Visor component should look innovative.

```html
<!DOCTYPE html>
<html lang="en">
<head>
<meta charset="utf-8">
<title>Korvix App Screens</title>
<link rel="stylesheet" href="https://fonts.googleapis.com/css2?family=Lato:wght@100;300;400&display=swap">
<style>
  :root {
    --teal-deep: #0a8aa3;
    --teal-bright: #1bbfd3;
    --sea-green: #5bae9e;
    --alert-red: #ef3d3f;
    --wood: #bfa276;
    --wood-dark: #a98a5c;
    --white: #ffffff;
    --page: #ffffff;
  }
  * { box-sizing: border-box; margin: 0; padding: 0; }
  html, body { width: 1200px; height: 1000px; overflow: hidden; background: var(--page); }
  body { position: relative; font-family: "Lato", sans-serif; color: var(--white); }

  .screen {
    position: absolute; top: 36px; width: 486px; height: 862px;
    background: linear-gradient(90deg, var(--wood-dark), var(--wood) 40%, var(--wood-dark));
    box-shadow: 0 14px 26px rgba(0,0,0,.45);
    overflow: hidden;
  }
  .screen--feed { left: 65px; }
  .screen--camera { left: 643px; }

  .topbar {
    position: absolute; left: 0; top: 0; width: 100%; height: 72px; z-index: 5;
    background: linear-gradient(90deg, var(--teal-deep), var(--teal-bright));
    box-shadow: 0 3px 6px rgba(0,0,0,.3);
  }
  .topbar__title {
    position: absolute; left: 0; right: 0; top: 10px; text-align: center;
    font-weight: 100; font-size: 44px; letter-spacing: 1px;
  }
  .icon { position: absolute; width: 46px; height: 46px; }
  .icon svg { width: 100%; height: 100%; display: block; }

  .photo {
    position: absolute;
    background: linear-gradient(180deg, #8d95c9 0%, #a4a8d0 30%, #b9b0cc 48%, #e4b4aa 58%, #a9a9c0 62%, #9ea2bb 72%, #707894 85%, #3c4660 100%);
  }
  .photo--feed { left: 27px; top: 72px; width: 433px; height: 790px;
    background: linear-gradient(180deg, #8d95c9 0%, #a4a8d0 28%, #b9b0cc 46%, #e4b4aa 54%, #aaa9c0 58%, #9ea2bb 66%, #5d6682 80%, #1f2840 100%); }
  .photo--camera { left: 26px; top: 72px; width: 434px; height: 632px; box-shadow: 0 6px 10px rgba(0,0,0,.45); }

  .visor {
    position: absolute; left: 27px; top: 72px; width: 433px; height: 87px; z-index: 3;
    background: linear-gradient(180deg, rgba(160,195,225,.75), rgba(40,140,185,.8));
    text-align: center; font-size: 20px; line-height: 28px; padding-top: 16px;
    box-shadow: 0 3px 4px rgba(0,0,0,.25);
  }
  .visor__fold { position: absolute; top: 72px; width: 27px; height: 87px; background: rgba(230,225,210,.55); z-index: 2; }
  .visor__fold--l { left: 0; }
  .visor__fold--r { right: 0; }

  .stats { position: absolute; top: 540px; left: 38px; width: 410px; display: flex; justify-content: space-between;
    font-weight: 300; font-size: 19px; color: rgba(255,255,255,.8); z-index: 3; }

  .ribbon { position: absolute; height: 60px; display: flex; align-items: center; font-weight: 300; font-size: 28px; z-index: 3; }
  .ribbon--promote { left: 14px; top: 579px; width: 209px; background: rgba(70,160,130,.85); padding-left: 39px; gap: 26px; }
  .ribbon--demote { left: 264px; top: 579px; width: 209px; background: rgba(230,50,55,.85); padding-left: 18px; gap: 20px; }
  .ribbon--place { left: 14px; top: 653px; width: 459px; background: rgba(10,125,135,.85); font-size: 20px; padding-left: 39px; }
  .ribbon svg { width: 30px; height: 30px; }
</style>
</head>
<body>

<section class="screen screen--feed" aria-label="Feed screen">
  <div class="photo photo--feed" role="img" aria-label="Photo of a lake at sunrise with moored sailboats under a lavender sky"></div>

  <header class="topbar">
    <span class="icon" style="left:36px;top:14px"><svg viewBox="0 0 46 46" fill="none" stroke="#fff" stroke-width="2"><path d="M3 13h34M3 22h34M3 31h34"/></svg></span>
    <h1 class="topbar__title">feed</h1>
    <span class="icon" style="left:403px;top:13px"><svg viewBox="0 0 46 46" fill="none" stroke="#fff" stroke-width="1.5"><circle cx="23" cy="23" r="21"/><circle cx="23" cy="23" r="4" fill="#fff"/></svg></span>
  </header>

  <div class="visor__fold visor__fold--l"></div>
  <div class="visor__fold visor__fold--r"></div>
  <div class="visor">Sunrise at Lake Merrow<br>#LakeMer#Sunrise#Holidays</div>

  <span class="icon" style="left:38px;top:180px"><svg viewBox="0 0 46 46" fill="none" stroke="#fff" stroke-width="1.5"><circle cx="23" cy="23" r="21"/><path d="M15 33V13c6-3 10 3 17 0v11c-7 3-11-3-17 0" fill="#fff"/></svg></span>
  <span class="icon" style="left:403px;top:180px"><svg viewBox="0 0 46 46" fill="none" stroke="#fff" stroke-width="1.5"><circle cx="23" cy="23" r="21"/><path d="M16 31c0-8 5-13 12-13M23 13h7v7" stroke-width="3"/></svg></span>

  <div class="stats"><span>328 Km</span><span>+48</span><span>30min Ago</span></div>

  <div class="ribbon ribbon--promote">Promote <svg viewBox="0 0 30 30" stroke="#fff" stroke-width="1.5"><path d="M15 1v28M1 15h28"/></svg></div>
  <div class="ribbon ribbon--demote"><svg viewBox="0 0 30 30" stroke="#fff" stroke-width="1.5"><path d="M4 4l22 22M26 4L4 26"/></svg> Demote</div>
  <div class="ribbon ribbon--place">Lake Merrow, Coastline, Ferra,</div>

  <span class="icon" style="left:38px;top:727px"><svg viewBox="0 0 46 46" fill="none" stroke="#fff" stroke-width="1.5"><circle cx="23" cy="23" r="21"/><rect x="12" y="16" width="22" height="15"/><circle cx="23" cy="23.5" r="4"/></svg></span>
  <span class="icon" style="left:403px;top:727px"><svg viewBox="0 0 46 46" fill="none" stroke="#fff" stroke-width="1.5"><circle cx="23" cy="23" r="21"/><path d="M19 11l-3 24M29 11l-3 24M12 18h23M11 28h23"/></svg></span>
</section>

<section class="screen screen--camera" aria-label="Camera screen">
  <header class="topbar">
    <span class="icon" style="left:38px;top:13px"><svg viewBox="0 0 46 46" fill="none" stroke="#fff" stroke-width="1.5"><circle cx="23" cy="23" r="21"/><path d="M8 8l30 30M25 11l-7 13h8l-5 12" /></svg></span>
    <span class="icon" style="left:122px;top:11px;width:60px;height:50px"><svg viewBox="0 0 60 50" fill="none" stroke="#fff" stroke-width="1.5"><ellipse cx="30" cy="25" rx="28" ry="14"/><rect x="18" y="16" width="24" height="17" fill="#1398b4"/><circle cx="30" cy="24.5" r="4"/><path d="M36 40l-4-2 3-3M24 10l4 2-3 3"/></svg></span>
    <span class="icon" style="left:306px;top:13px"><svg viewBox="0 0 46 46" fill="none" stroke="#fff" stroke-width="1.5"><circle cx="23" cy="23" r="21"/><path d="M11 23c6-8 18-8 24 0-6 6-18 6-24 0z" fill="#fff"/><circle cx="23" cy="21" r="3" fill="#1398b4" stroke="none"/></svg></span>
    <span class="icon" style="left:402px;top:13px"><svg viewBox="0 0 46 46" fill="none" stroke="#fff" stroke-width="1.5"><circle cx="23" cy="23" r="21"/><path d="M9 9l28 28M37 9L9 37"/></svg></span>
  </header>

  <div class="photo photo--camera" role="img" aria-label="Camera preview of a lake at sunrise with moored sailboats"></div>

  <span class="icon" style="left:26px;top:784px"><svg viewBox="0 0 46 46" fill="none" stroke="#fff" stroke-width="1.5"><circle cx="23" cy="23" r="21"/><rect x="13" y="16" width="16" height="16"/><path d="M17 16v-4h16v16h-4"/></svg></span>
  <span class="icon" style="left:123px;top:784px"><svg viewBox="0 0 46 46" stroke="#fff" stroke-width="1.5"><circle cx="23" cy="23" r="21" fill="none"/><path d="M8 11A21 21 0 0 0 35 38z" fill="#fff"/></svg></span>
  <span class="icon" style="left:219px;top:784px"><svg viewBox="0 0 46 46" fill="none" stroke="#fff" stroke-width="1.5"><circle cx="23" cy="23" r="21"/><rect x="12" y="16" width="22" height="15"/><circle cx="23" cy="23.5" r="4"/></svg></span>
  <span class="icon" style="left:316px;top:784px"><svg viewBox="0 0 46 46" fill="none" stroke="#fff" stroke-width="1.5"><circle cx="23" cy="23" r="21"/><path d="M13 19v-6h6M27 13h6v6M33 27v6h-6M19 33h-6v-6"/></svg></span>
  <span class="icon" style="left:413px;top:784px"><svg viewBox="0 0 46 46" fill="none" stroke="#fff" stroke-width="1.5"><circle cx="23" cy="23" r="21"/><circle cx="23" cy="23" r="17" fill="rgba(255,255,255,.35)"/></svg></span>
</section>

<div aria-label="Colour palette" style="position:absolute;left:479px;top:948px;display:flex;gap:13px">
  <span style="width:37px;height:38px;border-radius:6px;background:var(--teal-deep)"></span>
  <span style="width:37px;height:38px;border-radius:6px;background:var(--teal-bright)"></span>
  <span style="width:37px;height:38px;border-radius:6px;background:var(--sea-green)"></span>
  <span style="width:37px;height:38px;border-radius:6px;background:var(--alert-red)"></span>
  <span style="width:37px;height:38px;border-radius:6px;background:var(--wood)"></span>
</div>

</body>
</html>
```